Harborline Crest Insurance Services

we are a high end insurance agency we specialize on Auto | Home | Business | Life looking for something professional and luxuries at the same time. if you guys need anything else please let me know.

Auto | Home | Business | Life must be under logo on the back with black background.

i want the back part to be black with our gold logo on it.

Target Market(s)

Auto | Home | Business | Life

Industry/Entity Type

Insurance Broker

Contact Information for Business Card

My logo is gold so a black in the back would be nice.

Font styles to use
Serif

Colors
000000

Requirements
Must have
• Big logo on the back with black background.

```html
<!DOCTYPE html>
<html lang="en">
<head>
<meta charset="utf-8">
<title>Harborline Crest Insurance Services – Business Card</title>
<link rel="stylesheet" href="https://fonts.googleapis.com/css2?family=Cinzel:wght@500;700&display=swap">
<style>
  :root {
    --backdrop: #5c5c5e;
    --card-black: #03040a;
    --gold: #f2c225;
    --silver: #a9aaad;
    --divider: #4a4a4e;
  }
  * { margin: 0; padding: 0; box-sizing: border-box; }
  html, body {
    width: 1200px; height: 1200px; overflow: hidden;
    background: var(--backdrop);
  }
  .canvas { position: relative; width: 1200px; height: 1200px; }
  .card {
    position: absolute; left: 246px; width: 708px; height: 401px;
    background: var(--card-black);
    font-family: "Cinzel", Georgia, serif;
  }
  .card--front { top: 177px; }
  .card--back { top: 622px; }

  /* front */
  .front-mark {
    position: absolute; left: 284px; top: 52px;
    width: 140px; height: 140px; border-radius: 50%;
    background: var(--gold);
  }
  .front-name {
    position: absolute; left: 0; right: 0; top: 222px;
    text-align: center; color: var(--gold); font-weight: 700;
    line-height: 1.2;
  }
  .front-name .line-main { display: block; font-size: 42px; letter-spacing: 0.5px; }
  .front-name .line-sub { display: block; font-size: 17px; letter-spacing: 5px; }
  .service-list {
    position: absolute; left: 0; right: 0; top: 348px;
    display: flex; justify-content: center; align-items: center;
    list-style: none; color: var(--gold);
    font-size: 17px; font-weight: 700; letter-spacing: 2px;
  }
  .service-list li { padding: 0 15px; line-height: 22px; }
  .service-list li + li { border-left: 2px solid #e6e6e6; }

  /* back */
  .back-mark {
    position: absolute; left: 172px; top: 90px;
    width: 84px; height: 84px; border-radius: 50%;
    background: var(--gold);
  }
  .back-name {
    position: absolute; left: 272px; top: 104px;
    color: var(--gold); font-weight: 700; line-height: 1.15;
  }
  .back-name .line-main { display: block; font-size: 29px; }
  .back-name .line-sub { display: block; font-size: 11.5px; letter-spacing: 3.6px; }

  .holder {
    position: absolute; right: 438px; top: 290px; text-align: right;
  }
  .holder-name { color: var(--gold); font-size: 25px; font-weight: 700; letter-spacing: 0.5px; }
  .holder-role { color: var(--silver); font-size: 16px; font-weight: 700; margin-top: 2px; }
  .divider {
    position: absolute; left: 298px; top: 262px; width: 1px; height: 116px;
    background: var(--divider);
  }
  .contact-list {
    position: absolute; left: 324px; top: 281px; list-style: none;
  }
  .contact-list li {
    display: flex; align-items: center; height: 24.5px;
    color: var(--silver); font-size: 15px; font-weight: 700; letter-spacing: 0.3px;
  }
  .contact-list svg { width: 24px; height: 20px; margin-right: 11px; flex: none; }
</style>
</head>
<body>
<main class="canvas">
  <section class="card card--front">
    <div class="front-mark" aria-hidden="true"></div>
    <h1 class="front-name">
      <span class="line-main">Harborline Crest</span>
      <span class="line-sub">Insurance Services</span>
    </h1>
    <ul class="service-list">
      <li>Auto</li><li>Home</li><li>Business</li><li>Life</li>
    </ul>
  </section>

  <section class="card card--back">
    <div class="back-mark" aria-hidden="true"></div>
    <h2 class="back-name">
      <span class="line-main">Harborline Crest</span>
      <span class="line-sub">Insurance Services</span>
    </h2>

    <div class="holder">
      <p class="holder-name">Daniel Reyes</p>
      <p class="holder-role">Managing Partner</p>
    </div>
    <div class="divider"></div>

    <ul class="contact-list">
      <li>
        <svg viewBox="0 0 24 20" aria-hidden="true">
          <path d="M2 7c0-4 20-4 20 0v2h-5V7H7v2H2z" fill="#f2c225"/>
          <rect x="5" y="10" width="14" height="9" rx="1.5" fill="#f2c225"/>
          <circle cx="12" cy="14.5" r="2.5" fill="#03040a"/>
        </svg>
        +0 000-000-000
      </li>
      <li>
        <svg viewBox="0 0 24 20" aria-hidden="true">
          <rect x="1" y="3" width="22" height="15" fill="#f2c225"/>
          <path d="M1 3l11 9 11-9M1 18l8-7M23 18l-8-7" fill="none" stroke="#03040a" stroke-width="1.6"/>
        </svg>
        dreyes@harborlinecrest.com
      </li>
      <li>
        <svg viewBox="0 0 24 20" aria-hidden="true">
          <g fill="none" stroke="#f2c225" stroke-width="1.5">
            <circle cx="12" cy="10" r="8.5"/>
            <ellipse cx="12" cy="10" rx="4" ry="8.5"/>
            <path d="M3.5 10h17M5 5.5h14M5 14.5h14M12 1.5v17"/>
          </g>
        </svg>
        harborlinecrest.com
      </li>
    </ul>
  </section>
</main>
</body>
</html>
```